Law Firm Logo and Business Card Design

I need a logo and business card design for a law firm I just started. The law firm is named Law Office of Doreen K. Ashworth, LLC. The type of law I practice is Family Law, which includes divorce, custody, child support, alimony, property division, and the like. I would like to see designs that are unique and modern, yet sophisticated. I would also like to use the logo/design for my letterhead. I am not opposed to using some form of the scales of justice although I'd like something other than the typical, old fashioned scales of justice. I had considered a house made out of puzzle pieces with one puzzle piece pulled away from the others, with the logo text reading "Guiding families toward what's next, one piece at a time." However, I don't want that particular design to look juvenile. I also would not be opposed to some form of my initials on the logo -- my initials are DKA. I am open to any other ideas you may have. I would like to see raised designs/lettering, and/or metallic finish. I like the colors black, white, gold, silver, and/or teal.

Industry/Entity Type

Law Firm

```html
<!DOCTYPE html>
<html lang="en">
<head>
<meta charset="utf-8">
<title>Doreen K. Ashworth – Business Card</title>
<link rel="stylesheet" href="https://fonts.googleapis.com/css2?family=Montserrat:wght@300;400;600;700&display=swap">
<style>
  :root {
    --backdrop: #e9e7e3;
    --card-dark-1: #2c2c2e;
    --card-dark-2: #161617;
    --band-1: #5c5c5e;
    --band-2: #a9a7a5;
    --band-3: #6a6a6c;
    --gold-1: #9a7424;
    --gold-2: #f4dc92;
    --gold-3: #b88a2e;
    --text-light: #ffffff;
    --text-soft: #d6d6d6;
    --silver: #9c9b9a;
  }
  * { box-sizing: border-box; margin: 0; padding: 0; }
  html, body { width: 1200px; height: 1000px; overflow: hidden; }
  body {
    background: var(--backdrop);
    font-family: "Montserrat", sans-serif;
    color: var(--text-light);
    position: relative;
  }
  .card {
    position: absolute;
    width: 700px;
    height: 400px;
    border-radius: 30px;
    overflow: hidden;
    background: radial-gradient(ellipse at 60% 30%, var(--card-dark-1), var(--card-dark-2) 80%);
    box-shadow: 0 10px 30px rgba(0,0,0,.25);
  }
  .card--front { left: 80px; top: 60px; }
  .card--back { left: 420px; top: 540px; }

  .gold-rule {
    position: absolute;
    left: 0; right: 0;
    height: 6px;
    background: linear-gradient(90deg, var(--gold-1), var(--gold-3) 35%, var(--gold-2) 60%, var(--gold-3) 85%, var(--gold-1));
  }
  .silver-band {
    position: absolute;
    left: 0; right: 0; bottom: 0;
    background: linear-gradient(90deg, var(--band-1), var(--band-2) 50%, var(--band-3));
  }

  /* Front */
  .card--front .gold-rule { bottom: 76px; }
  .card--front .silver-band { height: 76px; }
  .brand {
    position: absolute;
    left: 110px; top: 118px;
    display: flex; align-items: center; gap: 26px;
  }
  .brand__mark {
    display: flex; align-items: center; gap: 10px;
    font-weight: 700; font-size: 40px; color: var(--silver);
    letter-spacing: 2px;
  }
  .brand__square { width: 16px; height: 16px; background: var(--gold-3); }
  .brand__name { font-weight: 700; font-size: 38px; letter-spacing: .5px; }
  .brand__tagline {
    font-weight: 300; font-size: 15px; letter-spacing: 3.6px;
    color: var(--text-soft); margin-top: 10px; white-space: nowrap;
  }
  .website {
    position: absolute; left: 0; right: 0; bottom: 22px;
    text-align: center; font-weight: 400; font-size: 22px; letter-spacing: .5px;
  }

  /* Back */
  .card--back .gold-rule { top: 178px; }
  .card--back .silver-band { top: 184px; }
  .office {
    position: absolute; left: 52px; top: 36px;
  }
  .office__label { font-weight: 700; font-size: 38px; letter-spacing: .5px; }
  .office__name { font-weight: 700; font-size: 30px; margin-top: 4px; }
  .office__suffix { font-weight: 400; font-size: 17px; }
  .office-mark {
    position: absolute; right: 54px; top: 72px;
    display: flex; align-items: center; gap: 8px;
    font-weight: 700; font-size: 30px; color: var(--silver); letter-spacing: 1px;
  }
  .office-mark .brand__square { width: 12px; height: 12px; }
  .address {
    position: absolute; left: 40px; top: 222px;
    font-size: 22px; font-weight: 400; line-height: 1.3; font-style: normal;
  }
  .address__heading { font-weight: 700; font-size: 22px; }
  .contact {
    position: absolute; right: 34px; bottom: 38px;
    text-align: right; font-size: 22px; line-height: 1.55;
  }
  .contact__row { display: flex; justify-content: flex-end; align-items: center; gap: 10px; }
  .contact__icon { width: 18px; height: 18px; }
</style>
</head>
<body>

<section class="card card--front" aria-label="Business card front">
  <div class="brand">
    <div class="brand__mark"><span class="brand__square"></span>DKA</div>
    <div>
      <div class="brand__name">Doreen K. Ashworth</div>
      <div class="brand__tagline">Guiding families toward what's next</div>
    </div>
  </div>
  <div class="gold-rule"></div>
  <div class="silver-band"></div>
  <div class="website">www.ashworthfamilylaw.com</div>
</section>

<section class="card card--back" aria-label="Business card back">
  <div class="office">
    <div class="office__label">LAW OFFICE OF</div>
    <div class="office__name">Doreen K. Ashworth, <span class="office__suffix">LLC.</span></div>
  </div>
  <div class="office-mark"><span class="brand__square"></span>DKA</div>
  <div class="gold-rule"></div>
  <div class="silver-band"></div>
  <address class="address">
    <div class="address__heading">Address</div>
    742 Harbor Point Ave.<br>
    Suite 310<br>
    Annapolis, MD 21403
  </address>
  <div class="contact">
    <div class="contact__row">443-555-0172
      <svg class="contact__icon" viewBox="0 0 18 18" aria-hidden="true">
        <rect x="4.5" y="1" width="9" height="16" rx="2" fill="none" stroke="#fff" stroke-width="1.6"/>
        <circle cx="9" cy="14" r="1" fill="#fff"/>
      </svg>
    </div>
    <div class="contact__row">doreen@ashworthfamilylaw.com
      <svg class="contact__icon" viewBox="0 0 18 18" aria-hidden="true">
        <rect x="1" y="4" width="16" height="11" fill="none" stroke="#fff" stroke-width="1.6"/>
        <path d="M1 4 L9 10.5 L17 4" fill="none" stroke="#fff" stroke-width="1.6"/>
      </svg>
    </div>
  </div>
</section>

</body>
</html>
```